Five steps to on-time delivery

We need a SIMPLE and EFFECTIVE one-pager to help get our customers to do what we need to help them.
We are a contract packing business.
Our customers send us their product for us to pack.
Eg. Customer sends us 20 tonne of nuts, we run through our production lines to make 150g bags (of nuts) you buy from the supermarket.
We are driven mad because our customers constantly ask us to pack things before we've got them - or the minute after we've received the last component.
We run with 100+ people, 3 shifts on a 20,000sq meter site. we handle 1,000's of transactions a day. We need to be in control. This starts with our customers understanding it takes time to plan, order, schedule, set up, start, run, etc.
This would certainly be part of a Starter Pack (Contact details, Delivery Standards, Account Application, etc) and then no doubt sent out again and again to repeat offenders.
I will attach an excel file (if i can) that indicates the sort of thing i'm after. Sheet 1 (5) is the closest i've got. other sheets show the 'journey' but discarded because too 'busy'. Has to be simple/engaging/effective.
I've been bold and had a pathetic go at being creative with the blurb down the side of the page. Otherwise i felt our audience would fall asleep (it's a pretty dry topic - and our customers don't want to be told what to do by one of their suppliers). I'm hoping you get the idea of what i was trying to do - over to you for the creative part.
ps. have also uploaded examples of stationery and CORVALE Delivery Standards - that we've been sending out to Customers for years (and they don't pay any attention).
Reason: have extended deadline due to files not uploading yesterday.
Procurement people. Operations. Manufacturers. Large and small. Mainly in food industry.
Business

```html
<!DOCTYPE html>
<html lang="en">
<head>
<meta charset="utf-8">
<title>5 Steps to On-Time Delivery</title>
<link href="https://fonts.googleapis.com/css2?family=Roboto+Condensed:ital,wght@0,300;0,400;0,700;1,300&display=swap" rel="stylesheet">
<style>
  :root {
    --red: #e4412f;
    --navy: #1f3275;
    --ink: #1a1a1a;
    --paper: #ffffff;
  }
  * { margin: 0; padding: 0; box-sizing: border-box; }
  html, body { width: 1200px; height: 900px; overflow: hidden; background: var(--paper); }
  body { font-family: "Roboto Condensed", "Arial Narrow", sans-serif; color: var(--ink); }
  .sheet { position: relative; width: 1200px; height: 900px; }

  .title {
    position: absolute; left: 110px; top: 92px; width: 560px;
    text-align: center; font-weight: 300; font-style: italic;
    font-size: 70px; line-height: 72px; letter-spacing: -0.5px;
  }
  .intro {
    position: absolute; left: 692px; top: 117px; width: 370px;
    font-size: 14.5px; line-height: 20px; font-weight: 400;
  }

  .step {
    position: absolute; top: 277px; width: 191px; height: 403px;
    border-left: 2px solid var(--red); border-right: 2px solid var(--red);
  }
  .step--navy { border-color: var(--navy); }
  .step__head {
    position: absolute; left: -2px; right: -2px; top: 0; height: 101px;
    background: var(--red); color: var(--paper);
    display: flex; align-items: center; padding-left: 6px;
  }
  .step--navy .step__head { background: var(--navy); }
  .step__pointer { position: absolute; left: 30px; top: 100px; }
  .step__num { font-size: 64px; font-weight: 300; line-height: 1; margin-right: 6px; }
  .step__label { font-size: 25px; font-weight: 300; line-height: 26px; text-transform: uppercase; }
  .step__items {
    position: absolute; left: 28px; top: 152px; right: 8px;
    list-style: none; font-size: 18px; font-weight: 300; line-height: 19.5px; text-transform: uppercase;
  }
  .step__items li { margin-bottom: 19.5px; }
  .step__items small { font-size: 10px; font-style: italic; margin-left: 6px; }
  .step__due {
    position: absolute; left: 28px; top: 370px;
    font-size: 12px; line-height: 12.5px; font-weight: 400; text-transform: uppercase;
  }
  .timeline-rule { position: absolute; left: 113px; width: 978px; height: 2px; background: var(--navy); }

  .brand {
    position: absolute; left: 895px; top: 730px; width: 131px; height: 80px;
    background: var(--red); color: var(--paper);
    font-weight: 700; font-size: 14px; padding: 45px 0 0 7px; white-space: nowrap;
  }
  .address {
    position: absolute; left: 902px; top: 815px;
    font-size: 14.5px; line-height: 20px; font-style: normal;
  }
</style>
</head>
<body>
<main class="sheet">
  <h1 class="title">5 STEPS TO<br>ON-TIME DELIVERY</h1>
  <p class="intro">In our commitment to customer satisfaction and affordable pricing please follow the step-by-step guidelines below for an on-time delivery of your product. If you have any questions please contact your Corvale representative. To find out more information on our delivery process visit our website www.corvale.net.au.</p>

  <section class="step" style="left:113px">
    <div class="step__head"><span class="step__num">1</span><span class="step__label">Forecasts</span></div>
    <svg class="step__pointer" width="42" height="32" viewBox="0 0 42 32"><polygon points="0,0 42,0 2,31" fill="var(--red)"/></svg>
    <ul class="step__items">
      <li>Capacity<br>Planning<small>6-12 MO.</small></li>
      <li>Purchasing<small>3 MO.</small></li>
    </ul>
    <p class="step__due">Required at least<br>4-12 weeks prior</p>
  </section>

  <section class="step" style="left:308px">
    <div class="step__head"><span class="step__num">2</span><span class="step__label">New Jobs</span></div>
    <svg class="step__pointer" width="42" height="32" viewBox="0 0 42 32"><polygon points="0,0 42,0 2,31" fill="var(--red)"/></svg>
    <ul class="step__items">
      <li>Trials</li>
      <li>Material<br>Specification</li>
      <li>Packing<br>Instructions</li>
      <li>Pricing</li>
    </ul>
    <p class="step__due">Required at least<br>4-12 weeks prior</p>
  </section>

  <section class="step" style="left:504px">
    <div class="step__head"><span class="step__num">3</span><span class="step__label">Purchase<br>Orders</span></div>
    <svg class="step__pointer" width="42" height="32" viewBox="0 0 42 32"><polygon points="0,0 42,0 2,31" fill="var(--red)"/></svg>
    <ul class="step__items">
      <li>Part(s)</li>
      <li>Quantities</li>
      <li>Prices</li>
      <li>Delivery Dates</li>
    </ul>
    <p class="step__due">Required at least<br>4-12 weeks prior</p>
  </section>

  <section class="step" style="left:701px">
    <div class="step__head"><span class="step__num">4</span><span class="step__label">Materials</span></div>
    <svg class="step__pointer" width="42" height="32" viewBox="0 0 42 32"><polygon points="0,0 42,0 2,31" fill="var(--red)"/></svg>
    <ul class="step__items">
      <li>All materials<br>received in full</li>
      <li>Agreed<br>specification</li>
      <li>Compliant with<br>Corvale delivery<br>standards</li>
    </ul>
    <p class="step__due">Required at least<br>1 week prior</p>
  </section>

  <section class="step step--navy" style="left:898px">
    <div class="step__head"><span class="step__num">5</span><span class="step__label">The Month</span></div>
    <svg class="step__pointer" width="42" height="32" viewBox="0 0 42 32"><polygon points="0,0 42,0 2,31" fill="var(--navy)"/></svg>
    <ul class="step__items">
      <li>Priorities<br>and materials<br>managed in<br>weekly buckets</li>
    </ul>
    <p class="step__due">Required at least<br>1 week prior</p>
  </section>

  <div class="timeline-rule" style="top:629px"></div>
  <div class="timeline-rule" style="top:678px"></div>

  <div class="brand">CORVALE LOGO HERE</div>
  <address class="address">28 - 30 HALDEN ROAD<br>MARROW PARK, VIC 3190<br>TEL 03 9000 4720</address>
</main>
</body>
</html>
```